looking for sleek business card to standout from the crowd!

We are a young biotechnology company looking to help you personalize your health through understanding your genetic make up. We need you help in making a clean but sleek business card design using our new logo. The goal? Any time we give our cards out, people say "nice card!" The feel we are going for is "modern-techy". We don't want to come across as an old, giant pharma company, but not trying to be a hipster either.

Target Market(s)

healthcare and biotechnology industry.

Industry/Entity Type

Biotechnology

Contact Information for Business Card

Info to include on the card will be NAME, TITLE, EMAIL, PHONE. The companies website (www.corvalinbio.com) should also be on the card some where. Would like the logo, when printed, to be raised.

Requirements
Must have
• The logo we have attached in the color it is in. Fonts for text should lean toward more professional/tech.
Nice to have
• Prefer white/light color background
Should not have
• cartoons, landscape backgrounds images.

```html
<!DOCTYPE html>
<html lang="en">
<head>
<meta charset="utf-8">
<title>Corvalin Business Card</title>
<link rel="stylesheet" href="https://fonts.googleapis.com/css2?family=Open+Sans:wght@400;600&display=swap">
<style>
  :root {
    --backdrop: #e9eaec;
    --card: #ffffff;
    --brand-green: #7cc242;
    --brand-blue: #2f7dc4;
    --ink-grey: #5a5d61;
    --rule-green: #9fd27a;
  }
  html, body {
    margin: 0;
    width: 1200px;
    height: 1200px;
    overflow: hidden;
    background: var(--backdrop);
    font-family: "Open Sans", Arial, sans-serif;
  }
  .business-card {
    position: absolute;
    left: 150px;
    top: 343px;
    width: 900px;
    height: 514px;
    background: var(--card);
    box-shadow: 0 10px 30px rgba(0,0,0,0.12);
  }
  .holder {
    position: absolute;
    left: 64px;
    top: 150px;
  }
  .holder-name {
    margin: 0;
    color: var(--brand-green);
    font-weight: 400;
    font-size: 40px;
    letter-spacing: 1px;
    line-height: 1;
    text-transform: uppercase;
  }
  .holder-title {
    margin: 10px 0 0;
    color: var(--ink-grey);
    font-weight: 400;
    font-size: 22px;
  }
  .contact-list {
    list-style: none;
    margin: 22px 0 0;
    padding: 0;
  }
  .contact-item {
    display: flex;
    align-items: center;
    gap: 10px;
    color: var(--ink-grey);
    font-size: 23px;
    line-height: 32px;
  }
  .contact-item svg {
    width: 18px;
    height: 18px;
    flex: none;
  }
  .contact-item .domain { color: var(--brand-blue); }
  .divider {
    position: absolute;
    left: 56px;
    top: 392px;
    width: 560px;
    height: 1.5px;
    background: var(--rule-green);
  }
  .company-name {
    position: absolute;
    left: 64px;
    top: 412px;
    margin: 0;
    color: var(--ink-grey);
    font-weight: 400;
    font-size: 56px;
    letter-spacing: 4px;
    line-height: 1;
  }
</style>
</head>
<body>
  <main class="business-card">
    <section class="holder">
      <h1 class="holder-name">John Doe</h1>
      <p class="holder-title">Director</p>
      <ul class="contact-list">
        <li class="contact-item">
          <svg viewBox="0 0 20 20" aria-hidden="true"><path d="M5 2c1 0 2 3 2 4s-2 1-1 3 3 4 5 5 2-1 3-1 4 1 4 2-2 3-3 3C8 18 2 12 2 5c0-1 2-3 3-3z" fill="var(--brand-blue)"/></svg>
          <span>123-456-7890</span>
        </li>
        <li class="contact-item">
          <svg viewBox="0 0 20 20" aria-hidden="true"><g fill="none" stroke="var(--brand-blue)" stroke-width="1.8"><circle cx="10" cy="10" r="8"/><ellipse cx="10" cy="10" rx="3.5" ry="8"/><path d="M2 10h16M3.5 5.5h13M3.5 14.5h13"/></g></svg>
          <span>www.<span class="domain">corvalinbio</span>.com</span>
        </li>
        <li class="contact-item">
          <svg viewBox="0 0 20 20" aria-hidden="true"><rect x="1" y="4" width="18" height="12" fill="var(--brand-blue)"/><path d="M1 4l9 7 9-7" fill="none" stroke="#fff" stroke-width="1.4"/></svg>
          <span>john@<span class="domain">corvalinbio</span>.com</span>
        </li>
      </ul>
    </section>
    <div class="divider"></div>
    <p class="company-name">CORVALIN</p>
  </main>
</body>
</html>
```